Wordpress Design Project (Penwarden)

We need a wordpress design for an established auction and real estate company based in Arkansas. The winning design will incorporate the colors of logo (red and black) creatively with an accent color in a very professional and clean layout. Client mentions liking the site http://www.trelorbidhouse.example/ as a general idea.

Industry/Entity Type

Real Estate

Requirements
Must have
• Creative use of color and layout. Client mentions "Keep the site business professional looking and easy to navigate." Navigation:
1) Home
2) Auctions
3) Real Estate Listings
4) Buyers
5) Sellers
6) About Us
7) News & Events
8) Contact Us

Colors will be those of logo (choice of images attached) and perhaps creative use of shades of those colors. Site will have slideshow (initial placeholder image attached)

Sidebar widgets will be:
- Upcoming Auctions
- Featured Listings
- Video player
- New blog inset
- email sign-up form
- social media links/icons for facebook, youtube, twitter, RSS
Nice to have
• Site will have numerous drop-dowm menu options. For the Real Estate Listings" navigation element, it'd be nice to have idea of the following drop-downs:
- Land & Recreation (5)
- Commercial (6)
- Residential (7)
- Homes with Acreage (8)
- Oil & Gas (9
Should not have
• do not use any gavels in the design

```html
<!DOCTYPE html>
<html lang="en">
<head>
<meta charset="utf-8">
<title>Wexford &amp; Penwarden Auctioneers &amp; Land Brokers</title>
<link href="https://fonts.googleapis.com/css2?family=Open+Sans:wght@400;600;700;800&display=swap" rel="stylesheet">
<style>
:root{
  --navy:#14284f;
  --navy-2:#1f3a6e;
  --red:#c0202b;
  --ink:#2b2b2b;
  --muted:#6e6e6e;
  --line:#dcdcdc;
  --paper:#ffffff;
  --panel:#f3f3f3;
  --gold:#d3a341;
  --gold-soft:#dcb560;
  --green:#7d9a55;
  --green-soft:#8ba564;
  --olive:#a7a56a;
  --grey-photo:#b3b3b3;
}
*{box-sizing:border-box;margin:0;padding:0}
html,body{width:857px;height:1200px;overflow:hidden;background:var(--paper)}
body{font-family:"Open Sans",Arial,sans-serif;color:var(--ink);font-size:8px;line-height:1.35}
.page{position:relative;width:610px;height:1200px;margin-left:124px}

/* header */
.site-header{height:82px;display:flex;align-items:center;justify-content:space-between}
.brand{display:flex;align-items:center;gap:9px}
.brand-mark{width:26px;height:26px;background:var(--navy)}
.brand-name{font-weight:700;color:var(--navy);font-size:12px;line-height:1.15;width:210px}
.contact{text-align:right;color:var(--red);font-weight:700;font-size:10px;line-height:1.5}

/* nav */
.main-nav{height:26px;background:var(--navy);display:flex;border-radius:3px 3px 0 0;overflow:hidden}
.main-nav a{color:#fff;text-decoration:none;font-size:7.5px;font-weight:600;text-transform:uppercase;padding:0 13px;display:flex;align-items:center;border-right:1px solid var(--navy-2)}
.main-nav a.active{background:var(--red)}

/* slideshow */
.slideshow{position:relative;height:194px;background:linear-gradient(180deg,var(--gold-soft),var(--gold))}
.for-sale{position:absolute;right:18px;top:14px;width:150px;background:#fff;padding:6px;box-shadow:0 2px 6px rgba(0,0,0,.35)}
.for-sale-tag{position:absolute;left:-8px;top:12px;background:var(--red);color:#fff;font-weight:800;font-size:11px;padding:3px 9px}
.for-sale-photo{height:98px;background:var(--green-soft)}
.for-sale-text{font-size:7px;color:var(--muted);padding-top:5px}
.slide-arrow{position:absolute;top:85px;width:16px;height:22px;background:rgba(0,0,0,.45);display:flex;align-items:center;justify-content:center}
.slide-arrow.prev{left:0}.slide-arrow.next{right:0}

/* content */
.content{display:flex;gap:18px;margin-top:12px}
.listings{width:397px}
.section-title{font-size:10px;font-weight:700;color:var(--navy);text-transform:uppercase;border-bottom:2px solid var(--red);padding-bottom:3px;margin-bottom:8px}
.listing{display:flex;gap:10px;padding:8px 0 10px;border-bottom:1px solid var(--line);height:143px}
.listing-photo{flex:0 0 125px;height:118px;border:3px solid #fff;box-shadow:0 0 0 1px var(--line)}
.listing-photo.p1{background:var(--green)}
.listing-photo.p2{background:var(--olive)}
.listing-photo.p3{background:var(--green-soft)}
.listing-photo.p4{background:var(--gold-soft)}
.listing-body{flex:1;display:flex;flex-direction:column}
.listing-title{color:var(--red);font-weight:700;font-size:8px;text-transform:uppercase;margin-bottom:3px}
.listing-desc{color:var(--muted);font-size:7px;margin-bottom:4px}
.listing-auction{font-size:7px;font-weight:700;color:var(--navy);text-transform:uppercase}
.listing-meta{font-size:7px;color:var(--ink)}
.listing-actions{margin-top:auto;display:flex;justify-content:space-between;align-items:center}
.listing-links{font-size:7px;color:var(--navy);font-weight:600}
.btn{background:var(--red);color:#fff;font-size:7px;font-weight:700;padding:3px 9px;border-radius:2px;white-space:nowrap}

/* sidebar */
.sidebar{width:195px}
.social{display:flex;gap:7px;margin-bottom:12px}
.social span{width:20px;height:20px;border-radius:50%;background:var(--navy)}
.social span:nth-child(2n){background:var(--red)}
.widget{margin-bottom:12px}
.widget-title{font-size:9.5px;font-weight:700;color:var(--navy);text-transform:uppercase;border-bottom:2px solid var(--red);padding-bottom:3px;margin-bottom:6px}
.signup{display:flex;flex-direction:column;gap:5px}
.field{height:18px;border:1px solid var(--line);background:var(--panel);font-size:7px;color:var(--muted);padding:3px 5px}
.signup-row{display:flex;gap:5px}
.signup-row .field{flex:1}
.video{position:relative;height:102px;background:var(--green-soft);display:flex;align-items:center;justify-content:center}
.video-bar{position:absolute;left:0;right:0;bottom:0;height:11px;background:rgba(0,0,0,.65)}
.event{display:flex;gap:7px;padding:5px 0;border-bottom:1px dotted var(--line)}
.event-date{flex:0 0 26px;height:28px;background:var(--red);color:#fff;text-align:center;font-weight:700;font-size:6.5px;line-height:1.1;padding-top:3px}
.event-date b{display:block;font-size:10px}
.event-text{font-size:7px;color:var(--muted)}
.blog-list{list-style:none}
.blog-list li{font-size:7px;color:var(--muted);padding:2px 0 2px 9px;position:relative}
.blog-list li::before{content:"";position:absolute;left:0;top:5px;width:4px;height:4px;background:var(--red)}
.mini-listing{display:flex;gap:7px;padding:5px 0;border-bottom:1px dotted var(--line)}
.mini-photo{flex:0 0 48px;height:36px;background:var(--green)}
.mini-text{font-size:7px;color:var(--muted)}
.mini-text b{color:var(--red);display:block}

/* footer */
.footer-nav{position:absolute;top:985px;left:0;width:610px;height:24px;background:var(--navy);display:flex;justify-content:center;align-items:center;gap:6px;color:#fff;font-size:7.5px;font-weight:600}
.footer-nav i{font-style:normal;color:#7d8fb3}
.footer-main{position:absolute;top:1020px;left:0;width:610px;height:118px;background:var(--panel);display:flex;justify-content:space-between;align-items:center;padding:0 14px}
.testimonial{width:330px;background:#fff;border:1px solid var(--line);padding:8px;display:flex;gap:8px}
.testimonial-photo{flex:0 0 44px;height:50px;background:var(--grey-photo)}
.testimonial h4{font-size:8px;color:var(--navy);text-transform:uppercase;margin-bottom:3px}
.testimonial p{font-size:7px;color:var(--muted)}
.testimonial cite{display:block;text-align:right;font-size:7px;color:var(--red);font-style:normal;margin-top:3px}
.copyright{position:absolute;top:1155px;left:0;width:610px;text-align:center;font-size:7px;color:var(--muted)}
</style>
</head>
<body>
<div class="page">

  <header class="site-header">
    <div class="brand">
      <div class="brand-mark"></div>
      <div class="brand-name">Wexford &amp; Penwarden Auctioneers &amp; Land Brokers, LLC</div>
    </div>
    <div class="contact">
      <div>Call: (501) 555-0142</div>
      <div>Email: info@wexfordpenwarden.example</div>
    </div>
  </header>

  <nav class="main-nav">
    <a class="active">Home</a><a>Auctions</a><a>Real Estate Listings</a><a>Buyers</a><a>Sellers</a><a>About Us</a><a>News &amp; Events</a><a>Contact Us</a>
  </nav>

  <section class="slideshow" role="img" aria-label="Slideshow photo: golden wheat field under a blue sky">
    <div class="for-sale">
      <div class="for-sale-tag">FOR SALE</div>
      <div class="for-sale-photo" role="img" aria-label="Photo of a farmhouse on green acreage"></div>
      <div class="for-sale-text">Homestead on 40 acres, Benton County. Bid online or onsite.</div>
    </div>
    <div class="slide-arrow prev"><svg width="6" height="9"><path d="M5 1L1 4.5L5 8" stroke="#fff" stroke-width="1.5" fill="none"/></svg></div>
    <div class="slide-arrow next"><svg width="6" height="9"><path d="M1 1L5 4.5L1 8" stroke="#fff" stroke-width="1.5" fill="none"/></svg></div>
  </section>

  <div class="content">
    <main class="listings">
      <h2 class="section-title">Featured Listings</h2>

      <article class="listing">
        <div class="listing-photo p1" role="img" aria-label="Photo of green pasture land"></div>
        <div class="listing-body">
          <div class="listing-title">175 Acres Garfield &amp; Noble County</div>
          <p class="listing-desc">Rolling pasture with two stocked ponds, perimeter fencing and paved road frontage. Ideal for cattle, hay production or a private country homesite.</p>
          <div class="listing-auction">Live Onsite Auction with Online Bidding</div>
          <div class="listing-meta">Begins: Tuesday, May 22, 2012 at 10:00 AM CST</div>
          <div class="listing-meta">Location: Enid, Oklahoma</div>
          <div class="listing-actions"><span class="listing-links">Details | Photos | Virtual Tour</span><span class="btn">Read more</span></div>
        </div>
      </article>

      <article class="listing">
        <div class="listing-photo p2" role="img" aria-label="Photo of an open hay meadow"></div>
        <div class="listing-body">
          <div class="listing-title">80 Acres Hay Meadow, Carroll County</div>
          <p class="listing-desc">Productive hay meadow with a barn, well water and electric on site. Easy access from the highway and only minutes from town services.</p>
          <div class="listing-auction">Live Onsite Auction with Online Bidding</div>
          <div class="listing-meta">Begins: Thursday, May 31, 2012 at 10:00 AM CST</div>
          <div class="listing-meta">Location: Berryville, Arkansas</div>
          <div class="listing-actions"><span class="listing-links">Details | Photos | Virtual Tour</span><span class="btn">Read more</span></div>
        </div>
      </article>

      <article class="listing">
        <div class="listing-photo p3" role="img" aria-label="Photo of wooded recreational land"></div>
        <div class="listing-body">
          <div class="listing-title">240 Acres Recreation Land, Searcy County</div>
          <p class="listing-desc">Mixed hardwood timber with creek frontage, food plots and trails. Excellent hunting tract with a cabin site overlooking the valley below.</p>
          <div class="listing-auction">Live Onsite Auction with Online Bidding</div>
          <div class="listing-meta">Begins: Saturday, June 9, 2012 at 10:00 AM CST</div>
          <div class="listing-meta">Location: Marshall, Arkansas</div>
          <div class="listing-actions"><span class="listing-links">Details | Photos | Virtual Tour</span><span class="btn">Read more</span></div>
        </div>
      </article>

      <article class="listing">
        <div class="listing-photo p4" role="img" aria-label="Photo of cropland"></div>
        <div class="listing-body">
          <div class="listing-title">120 Acres Row Crop Farm, Lonoke County</div>
          <p class="listing-desc">Irrigated cropland with a shop building and grain bins. Strong yield history and level fields ready for the next planting season.</p>
          <div class="listing-auction">Live Onsite Auction with Online Bidding</div>
          <div class="listing-meta">Begins: Tuesday, June 19, 2012 at 10:00 AM CST</div>
          <div class="listing-meta">Location: Lonoke, Arkansas</div>
          <div class="listing-actions"><span class="listing-links">Details | Photos | Virtual Tour</span><span class="btn">Read more</span></div>
        </div>
      </article>
    </main>

    <aside class="sidebar">
      <div class="social"><span></span><span></span><span></span><span></span></div>

      <section class="widget">
        <h3 class="widget-title">Sign Up to E-Mail</h3>
        <div class="signup">
          <div class="field">Your name</div>
          <div class="signup-row"><div class="field">Email address</div><span class="btn">Submit</span></div>
        </div>
      </section>

      <section class="widget">
        <h3 class="widget-title">Featured Video</h3>
        <div class="video" role="img" aria-label="Video still of a farmhouse property">
          <svg width="26" height="26" viewBox="0 0 26 26"><circle cx="13" cy="13" r="12" fill="rgba(0,0,0,.55)"/><path d="M10 8L18 13L10 18Z" fill="#fff"/></svg>
          <div class="video-bar"></div>
        </div>
      </section>

      <section class="widget">
        <h3 class="widget-title">Upcoming Auctions</h3>
        <div class="event"><div class="event-date"><b>22</b>MAY</div><div class="event-text">175 acres of pasture land with ponds, fencing and road frontage.</div></div>
        <div class="event"><div class="event-date"><b>31</b>MAY</div><div class="event-text">80 acre hay meadow with barn and well water near town.</div></div>
        <div class="event"><div class="event-date"><b>09</b>JUN</div><div class="event-text">240 acres of timber and recreation land with a creek.</div></div>
      </section>

      <section class="widget">
        <h3 class="widget-title">New Blog Inset</h3>
        <ul class="blog-list">
          <li>Spring land market update</li>
          <li>Bidding online: a quick guide</li>
          <li>Vintage tractor auction recap</li>
          <li>Preparing your farm for sale</li>
          <li>Timber value basics for owners</li>
        </ul>
      </section>

      <section class="widget">
        <h3 class="widget-title">Featured Listings</h3>
        <div class="mini-listing"><div class="mini-photo" role="img" aria-label="Photo of a pasture listing"></div><div class="mini-text"><b>Pasture Land</b>Fenced acreage with ponds and good access.</div></div>
        <div class="mini-listing"><div class="mini-photo" role="img" aria-label="Photo of a country home listing"></div><div class="mini-text"><b>Country Home</b>Three bedroom home on twelve acres.</div></div>
      </section>
    </aside>
  </div>

  <nav class="footer-nav">
    <span>Home</span><i>|</i><span>Auctions</span><i>|</i><span>Real Estate Listings</span><i>|</i><span>Buyers</span><i>|</i><span>Sellers</span><i>|</i><span>About Us</span><i>|</i><span>News &amp; Events</span><i>|</i><span>Contact Us</span>
  </nav>

  <section class="footer-main">
    <div class="testimonial">
      <div class="testimonial-photo" role="img" aria-label="Client portrait photo"></div>
      <div>
        <h4>Client Testimonial</h4>
        <p>The team handled every detail of our farm sale with care. The auction drew strong bidders and the result beat our expectations by a wide margin.</p>
        <cite>— D. Hollis</cite>
      </div>
    </div>
    <div class="brand">
      <div class="brand-mark"></div>
      <div class="brand-name">Wexford &amp; Penwarden Auctioneers &amp; Land Brokers, LLC</div>
    </div>
  </section>

  <p class="copyright">Copyright © 2012 · Wexford &amp; Penwarden Auctioneers &amp; Land Brokers, LLC · All Rights Reserved · www.trelorbidhouse.example</p>

</div>
</body>
</html>
```